lunetra.com redesign

We are a successful web hosting company that has been around since 1999 with 10,000 customers managing 2,000 websites and 12,000 domain names. Our challenge - we are losing ground because our site is getting old, our pricing is not competitive and our feature set needs to change to match the new world of mobile centric everything. We want to reach out to all of the domain names that we don't host websites for. We believe that if we designed a new site that focuses on bringing home all of those externally hosted websites to our own web hosting company that we would have a solid future. We need to compete against mopwizzle.com, vantrimble.com, kerbloom.com, zinqhut.com, nolvark.com, brimfolk.com, quorvane.com, welbix.com and 100,000 others. We need to simplify our message with clean design, focused pages, easy decision making processes for the consumer. We use WHMCS for the background provisioning and billing so we can pretty much manage any kind of pricing model and discounted promotion packages.
I would prefer Chirper bootstrap CSS based responsive design.

Reason: I was away on vacation for 2 weeks - I just got back - I need time to fairly review all submissions - thank you for your patience. Dorian Fenwick Lunetra.com

Thanks to all who submitted sample designs - unfortunately most of them were nothing much more than already available templates with some of my current content and logo added to them. I will try to be more specific to reduce the number of choices. I need the template be fully compatible with WHMCS and Wordpress if you can't make it work with WHMCS directly. Another question I have to ask is -"exactly what am I getting for my $500.00 - is it just a PSD template or actual integration of that theme into WHMCS or Wordpress?"  I don't expect anyone to create new content for the site at that price. What do you charge if  you are able to create content or get directly involved in the site implementation of that template?

```html
<!DOCTYPE html>
<html lang="en">
<head>
<meta charset="utf-8">
<title>Lunetra — Unlimited Web Hosting</title>
<link href="https://fonts.googleapis.com/css2?family=Carlito:ital,wght@0,400;0,700;1,400&family=Jost:ital,wght@1,400;1,500&display=swap" rel="stylesheet">
<style>
:root{
  --brand:#4a78e6;
  --brand-dark:#3e69d6;
  --brand-line:#6b91ee;
  --ink:#1c1c1c;
  --muted:#6f6f6f;
  --rule:#d8d8d8;
  --white:#ffffff;
  --sky-top:#f4f7fb;
  --sky-bottom:#d6e3f0;
  --hardware:#1e2329;
  --rack:#2a2e34;
  --orange-light:#fbab3f;
  --orange-dark:#e0700a;
}
*{box-sizing:border-box;margin:0;padding:0}
html,body{width:931px;height:1200px;overflow:hidden;background:var(--white)}
body{font-family:"Carlito",Arial,sans-serif;color:var(--ink)}
.page{position:relative;width:931px;height:1200px;overflow:hidden}
.abs{position:absolute}

/* header */
.brand{left:148px;top:8px;font:700 44px/1 "Carlito",sans-serif;color:var(--brand);letter-spacing:-1px}
.topbar{left:311px;top:0;width:620px;height:58px;background:var(--brand)}
.utility-nav{left:429px;top:10px;display:flex;gap:21px;font-size:9px;color:var(--white)}
.main-nav{left:338px;top:35px;display:flex;font-size:10.5px;color:var(--white)}
.main-nav span{padding:0 7px;border-left:1px solid var(--brand-line)}
.main-nav span:first-child{border-left:0}

/* hero */
.hero-sky{left:0;top:58px;width:931px;height:366px;background:linear-gradient(180deg,var(--sky-top),var(--sky-bottom))}
.hero-title{left:0;top:80px;width:931px;text-align:center;font-family:"Jost",sans-serif;font-style:italic}
.hero-title .line1{font-size:24px;line-height:30px;color:var(--ink);padding-left:10px}
.hero-title .line1 em{color:var(--brand)}
.hero-title .line2{font-size:31px;line-height:34px;color:var(--brand);letter-spacing:1px}
.hero-visual{left:38px;top:157px;width:858px;height:267px;background:var(--hardware)}
.domain-search{left:308px;top:193px;width:340px;height:33px;background:var(--brand);display:flex;align-items:center;padding-left:13px;font-size:16px;color:var(--white)}
.domain-search svg{position:absolute;right:8px;top:5px}
.feature-list{list-style:none;font-size:10px;color:var(--white)}
.feature-list li{display:flex;align-items:center;gap:7px;height:17.5px}
.feature-list .tick{width:14px;height:14px;border:1.5px solid var(--white);display:flex;align-items:center;justify-content:center}
.list-left{left:320px;top:257px}
.list-right{left:496px;top:260px}
.cta-start{left:422px;top:358px;width:108px;height:33px;background:linear-gradient(180deg,var(--orange-light),var(--orange-dark));color:var(--white);font-size:16px;display:flex;align-items:center;justify-content:center}

/* promo band */
.promo-band{left:0;top:424px;width:931px;height:77px;background:var(--brand);color:var(--white);font-size:24px;display:flex;align-items:center;justify-content:center}

/* benefits */
.benefit{top:518px;width:150px;text-align:center}
.benefit .icon{height:40px;display:flex;justify-content:center;align-items:flex-end}
.benefit h3{font-weight:400;font-size:12.5px;color:var(--brand);margin-top:8px;height:25px}
.benefit p{font-size:9.5px;line-height:14.5px;color:var(--muted);width:132px;margin:0 auto}
.benefit-divider{top:530px;width:1px;height:126px;background:var(--rule)}
.learn-more{top:670px;width:88px;height:21px;border:1px solid var(--brand);border-radius:2px;font-size:9.5px;color:var(--brand);display:flex;align-items:center;padding-left:7px}
.learn-more svg{position:absolute;right:6px;top:4px}

/* plans */
.section-title{left:0;top:722px;width:931px;text-align:center;font-size:20px;font-weight:400;color:var(--brand)}
.section-title strong{font-weight:700;color:var(--brand-dark)}
.plans-backdrop{left:0;top:758px;width:931px;height:252px;background:linear-gradient(180deg,#9ea2a8 0%,var(--rack) 25%,var(--rack))}
.plan{top:790px;width:145px;background:var(--white);border-radius:3px;overflow:hidden}
.plan h4{height:22px;background:var(--brand);color:var(--white);font-weight:400;font-size:14px;padding-left:13px;line-height:22px}
.plan table{width:100%;border-collapse:collapse;font-size:9.5px}
.plan td{border-top:1px solid #e1e1e1;vertical-align:top;padding:7px 0 0 13px;line-height:12.5px}
.plan td.label{width:66px;color:var(--brand);border-right:1px solid #e1e1e1}
.plan td.value{color:var(--muted);padding-left:12px}
.plan tr.r1 td{height:30px}
.plan tr.r2 td{height:33px}
.plan tr.r3 td{height:40px}
.plan tr.price td{height:37px;border-top:1px solid #444;padding-top:6px}
.plan tr.price td.label{color:var(--ink);border-right:0}
.plan tr.price td.value{font-size:22px;color:var(--brand);padding:6px 0 0 4px;line-height:1}
.see-all{left:405px;top:969px;width:117px;height:22px;background:var(--brand);color:var(--white);font-size:9.5px;display:flex;align-items:center;padding-left:7px}
.see-all svg{position:absolute;right:6px;top:4px}

/* footer */
.site-footer{left:0;top:1010px;width:931px;height:190px;background:var(--brand)}
.footer-col{top:1027px;color:var(--white)}
.footer-col h5{font-weight:400;font-size:17px;line-height:20px;margin-bottom:2px}
.footer-col ul{list-style:none}
.footer-col li{font-size:9.5px;line-height:16px}
.footer-col.tight li{line-height:12px}
.footer-divider{top:1012px;width:1px;height:126px;background:var(--brand-line)}
.footer-rule{left:0;top:1138px;width:931px;height:1px;background:var(--brand-line)}
.social{left:168px;top:1153px;display:flex;gap:8px;font-size:10px;color:var(--white)}
.payments{left:399px;top:1152px;display:flex;gap:10px}
.payments span{width:32px;height:20px;background:var(--white);color:var(--brand-dark);font-size:8px;display:flex;align-items:center;justify-content:center;border-radius:2px}
.footer-brand{left:606px;top:1146px;font:700 44px/1 "Carlito",sans-serif;color:var(--white);letter-spacing:-1px}
.copyright{left:166px;top:1179px;font-size:8.5px;color:var(--white)}
</style>
</head>
<body>
<div class="page">

  <header>
    <div class="abs brand">lunetra</div>
    <div class="abs topbar"></div>
    <nav class="abs utility-nav">
      <span>Monday, 17 March 2014</span><span>Company</span><span>Partners</span><span>Contact us</span><span>Shopping cart</span><span>Pricing</span>
    </nav>
    <nav class="abs main-nav">
      <span>Home</span><span>Domain Name Center</span><span>Web Site Hosting Center</span><span>S.E.O Toolkit</span><span>Support</span><span>Client Area</span>
    </nav>
  </header>

  <div class="abs hero-sky" role="img" aria-label="Soft sky with clouds"></div>
  <div class="abs hero-visual" role="img" aria-label="Laptop between glossy black server towers with blue lights"></div>
  <div class="abs hero-title">
    <div class="line1">Unlimited Web Hosting <em>Web Hosting made</em></div>
    <div class="line2">EASY and AFFORDABLE!</div>
  </div>

  <div class="abs domain-search">www.yourname.com
    <svg width="24" height="24" viewBox="0 0 24 24"><circle cx="10" cy="10" r="7" fill="none" stroke="#111" stroke-width="2.5"/><line x1="15" y1="15" x2="22" y2="22" stroke="#111" stroke-width="3.5"/></svg>
  </div>
  <ul class="abs feature-list list-left">
    <li><span class="tick"><svg width="10" height="10"><path d="M1 5l3 3 5-7" fill="none" stroke="#fff" stroke-width="2"/></svg></span>UNLIMITED Disk Space</li>
    <li><span class="tick"><svg width="10" height="10"><path d="M1 5l3 3 5-7" fill="none" stroke="#fff" stroke-width="2"/></svg></span>UNLIMITED Bandwidth</li>
    <li><span class="tick"><svg width="10" height="10"><path d="M1 5l3 3 5-7" fill="none" stroke="#fff" stroke-width="2"/></svg></span>EASY Control Panel (Try Demo)</li>
    <li><span class="tick"><svg width="10" height="10"><path d="M1 5l3 3 5-7" fill="none" stroke="#fff" stroke-width="2"/></svg></span>1-CLICK Script Installs</li>
    <li><span class="tick"><svg width="10" height="10"><path d="M1 5l3 3 5-7" fill="none" stroke="#fff" stroke-width="2"/></svg></span>$100 Searchly Ads Offer</li>
  </ul>
  <ul class="abs feature-list list-right">
    <li><span class="tick"><svg width="10" height="10"><path d="M1 5l3 3 5-7" fill="none" stroke="#fff" stroke-width="2"/></svg></span>4,500 Free Website Templates</li>
    <li><span class="tick"><svg width="10" height="10"><path d="M1 5l3 3 5-7" fill="none" stroke="#fff" stroke-width="2"/></svg></span>99.9% Uptime Guarantee</li>
    <li><span class="tick"><svg width="10" height="10"><path d="M1 5l3 3 5-7" fill="none" stroke="#fff" stroke-width="2"/></svg></span>45 Day Money Back Guarantee</li>
    <li><span class="tick"><svg width="10" height="10"><path d="M1 5l3 3 5-7" fill="none" stroke="#fff" stroke-width="2"/></svg></span>24/7/365 Technical Support</li>
  </ul>
  <div class="abs cta-start">START NOW</div>

  <div class="abs promo-band">Sale! Premium top-level domain names from $15/year.</div>

  <section>
    <div class="abs benefit" style="left:141px">
      <div class="icon"><svg width="38" height="36" viewBox="0 0 38 36"><rect x="2" y="5" width="30" height="26" fill="none" stroke="#4a78e6" stroke-width="1.5"/><rect x="2" y="5" width="30" height="5" fill="#4a78e6"/><g fill="#4a78e6"><rect x="7" y="14" width="3" height="3"/><rect x="13" y="14" width="3" height="3"/><rect x="19" y="14" width="3" height="3"/><rect x="25" y="14" width="3" height="3"/><rect x="7" y="20" width="3" height="3"/><rect x="13" y="20" width="3" height="3"/><rect x="19" y="20" width="3" height="3"/><rect x="7" y="25" width="3" height="3"/><rect x="13" y="25" width="3" height="3"/></g><path d="M28 26c2 4 5 6 8 5" fill="none" stroke="#4a78e6" stroke-width="2"/></svg></div>
      <h3>24/7 Customer Service</h3>
      <p>Trained, in-house experts are here to help 24/7. Our robust help center includes guides, video tutorials and more.</p>
    </div>
    <div class="abs benefit-divider" style="left:297px"></div>
    <div class="abs benefit" style="left:300px">
      <div class="icon"><svg width="40" height="34" viewBox="0 0 40 34"><rect x="4" y="4" width="30" height="18" fill="none" stroke="#4a78e6" stroke-width="1.5"/><rect x="1" y="8" width="30" height="18" fill="#fff" stroke="#4a78e6" stroke-width="1.5"/><text x="9" y="22" font-size="13" fill="#4a78e6" font-family="Carlito,sans-serif">[$]</text><circle cx="32" cy="26" r="6" fill="#4a78e6"/><path d="M29 26l2 2 4-4" fill="none" stroke="#fff" stroke-width="1.5"/></svg></div>
      <h3 style="margin-top:4px">Money-back guarantee</h3>
      <p>Try us and love us, or get a refund any time. You're never locked into a contract and there are no hidden fees or gimmicks.</p>
    </div>
    <div class="abs benefit-divider" style="left:458px"></div>
    <div class="abs benefit" style="left:464px">
      <div class="icon"><svg width="30" height="40" viewBox="0 0 30 40"><path d="M9 8H2v30h26V8h-7" fill="none" stroke="#4a78e6" stroke-width="1.5"/><line x1="15" y1="0" x2="15" y2="16" stroke="#4a78e6" stroke-width="1.5"/><path d="M10 11l5 5 5-5" fill="none" stroke="#4a78e6" stroke-width="1.5"/><text x="11" y="33" font-size="12" fill="#4a78e6" font-family="Carlito,sans-serif">1</text></svg></div>
      <h3>one-click installs</h3>
      <p>Tessel Marketplace is integrated directly into your account, making the web's most popular resources instantly</p>
    </div>
    <div class="abs benefit-divider" style="left:618px"></div>
    <div class="abs benefit" style="left:627px">
      <div class="icon"><svg width="36" height="38" viewBox="0 0 36 38"><g fill="none" stroke="#4a78e6" stroke-width="1.5"><rect x="2" y="2" width="14" height="14"/><rect x="20" y="2" width="14" height="14"/><rect x="2" y="22" width="14" height="14"/><rect x="20" y="22" width="14" height="14"/></g></svg></div>
      <h3>over $200 in offers</h3>
      <p>Enjoy advertising offers from Searchly, free credits from Friendora and other leading sites to help grow your business - all included.</p>
    </div>
    <div class="abs learn-more" style="left:171px">learn more<svg width="8" height="13"><path d="M1 1l6 5.5L1 12" fill="none" stroke="#4a78e6" stroke-width="1.3"/></svg></div>
    <div class="abs learn-more" style="left:331px">learn more<svg width="8" height="13"><path d="M1 1l6 5.5L1 12" fill="none" stroke="#4a78e6" stroke-width="1.3"/></svg></div>
    <div class="abs learn-more" style="left:495px">learn more<svg width="8" height="13"><path d="M1 1l6 5.5L1 12" fill="none" stroke="#4a78e6" stroke-width="1.3"/></svg></div>
    <div class="abs learn-more" style="left:659px">learn more<svg width="8" height="13"><path d="M1 1l6 5.5L1 12" fill="none" stroke="#4a78e6" stroke-width="1.3"/></svg></div>
  </section>

  <h2 class="abs section-title">Choose a <strong>hosting package</strong></h2>
  <div class="abs plans-backdrop" role="img" aria-label="Data centre server racks with status lights"></div>

  <div class="abs plan" style="left:163px"><h4>Starter Plan</h4><table>
    <tr class="r1"><td class="label">Storage</td><td class="value">100MB</td></tr>
    <tr class="r2"><td class="label">Domain<br>name</td><td class="value">Included</td></tr>
    <tr class="r3"><td class="label">Email<br>Accounts</td><td class="value">Unlimited</td></tr>
    <tr class="price"><td class="label">Annual<br>Price</td><td class="value">$90</td></tr></table></div>
  <div class="abs plan" style="left:319px"><h4>Super Saving Plan</h4><table>
    <tr class="r1"><td class="label">Storage</td><td class="value">500MB</td></tr>
    <tr class="r2"><td class="label">Domain<br>name</td><td class="value">Included</td></tr>
    <tr class="r3"><td class="label">Email<br>Accounts</td><td class="value">Unlimited</td></tr>
    <tr class="price"><td class="label">Annual<br>Price</td><td class="value">$90</td></tr></table></div>
  <div class="abs plan" style="left:478px"><h4>Super Storage Plan</h4><table>
    <tr class="r1"><td class="label">Storage</td><td class="value">1GB</td></tr>
    <tr class="r2"><td class="label">Domain<br>name</td><td class="value">Included</td></tr>
    <tr class="r3"><td class="label">Email<br>Accounts</td><td class="value">Unlimited</td></tr>
    <tr class="price"><td class="label">Annual<br>Price</td><td class="value">$90</td></tr></table></div>
  <div class="abs plan" style="left:635px"><h4>Premium Plan</h4><table>
    <tr class="r1"><td class="label">Storage</td><td class="value">100MB</td></tr>
    <tr class="r2"><td class="label">Domain<br>name</td><td class="value">Included</td></tr>
    <tr class="r3"><td class="label">Email<br>Accounts</td><td class="value">Unlimited</td></tr>
    <tr class="price"><td class="label">Annual<br>Price</td><td class="value">$90</td></tr></table></div>
  <div class="abs see-all">see all package<svg width="8" height="13"><path d="M1 1l6 5.5L1 12" fill="none" stroke="#fff" stroke-width="1.3"/></svg></div>

  <footer class="abs site-footer"></footer>
  <div class="abs footer-col" style="left:170px"><h5>products</h5><ul><li>shared hosting</li><li>vps hosting</li><li>dedicated hosting</li><li>hosting features</li><li>reseller hosting</li></ul></div>
  <div class="abs footer-divider" style="left:287px"></div>
  <div class="abs footer-col tight" style="left:320px"><h5>programs</h5><ul><li>affiliates</li><li>education</li></ul></div>
  <div class="abs footer-divider" style="left:447px"></div>
  <div class="abs footer-col tight" style="left:493px"><h5>support</h5><ul><li>chat</li><li>ticket</li><li>system status</li><li>knowledge base</li></ul></div>
  <div class="abs footer-divider" style="left:615px"></div>
  <div class="abs footer-col tight" style="left:666px"><h5>company</h5><ul><li>about</li><li>contact</li><li>terms of service</li><li>privacy policy</li><li>blog</li></ul></div>
  <div class="abs footer-rule"></div>
  <div class="abs social"><span>Friendora</span><span>Plusring</span><span>Chirper</span><span>Feed</span></div>
  <div class="abs payments"><span>Paywren</span><span>Vantor</span><span>Mintcard</span></div>
  <div class="abs footer-brand">lunetra</div>
  <div class="abs copyright">Copyright © 2014 Lunetra.com All Rights Reserved.</div>

</div>
</body>
</html>
```